PowerPoint presentation for new Building Certification business

We are Harbourline Approval Group.

We are a young company providing a modern service in an industry that was predominately provided by inefficient local Council's who did not complete with anyone for work.

We are after a PowerPoint slide for presentations we hope to give prospective clients. The title page is to include a flash design that draws attention to our logo.

We also require an additional page for the body of the presentation. This is to be modern and simplistic but clearly recognisable with our brand and logo.

Target Market(s)

Architects. Draftsman. Developers. Project managers. Builders. Home owners.

Industry/Entity Type

Industry

Requirements
Must have
• Corporate logo and colours.
• Flash design to title page that involves our logo

```html
<!DOCTYPE html>
<html lang="en">
<head>
<meta charset="utf-8">
<title>Harbourline Approval Group — Project Slide</title>
<link rel="stylesheet" href="https://fonts.googleapis.com/css2?family=Oswald:wght@600;700&family=Lora:wght@400&display=swap">
<style>
  :root {
    --stripe-deep: #5a6fc4;
    --stripe-mid: #7183d0;
    --band-light: #e6ebfd;
    --navy: #1d2a8f;
    --body-grey: #4a4a55;
    --accent-soft: #aab8f4;
  }
  html, body {
    margin: 0;
    padding: 0;
    width: 1200px;
    height: 900px;
    overflow: hidden;
  }
  .slide {
    position: relative;
    width: 1200px;
    height: 900px;
    overflow: hidden;
    background:
      linear-gradient(to bottom,
        rgba(230,235,253,0) 0%,
        rgba(230,235,253,0.55) 16%,
        rgba(230,235,253,0.97) 32%,
        rgba(230,235,253,1) 45%,
        rgba(230,235,253,0.97) 58%,
        rgba(230,235,253,0.55) 76%,
        rgba(230,235,253,0) 100%),
      repeating-linear-gradient(to right,
        var(--stripe-deep) 0px, var(--stripe-deep) 6px,
        var(--stripe-mid) 6px, var(--stripe-mid) 15px);
  }
  .brand {
    position: absolute;
    left: 123px;
    top: 360px;
    width: 330px;
    text-align: center;
    font-family: "Oswald", sans-serif;
    font-weight: 600;
    color: var(--navy);
  }
  .brand-mark {
    display: block;
    width: 78px;
    height: 78px;
    margin: 0 auto 22px;
    background: var(--navy);
  }
  .brand-name {
    margin: 0;
    font-size: 46px;
    line-height: 1.05;
    letter-spacing: 2px;
    text-transform: uppercase;
  }
  .brand-name .line-small {
    display: block;
    font-size: 24px;
    letter-spacing: 6px;
    margin-top: 6px;
  }
  .project {
    position: absolute;
    left: 527px;
    top: 372px;
    width: 500px;
  }
  .project-title {
    margin: 0 0 14px;
    font-family: "Oswald", sans-serif;
    font-weight: 700;
    font-size: 42px;
    letter-spacing: 3px;
    color: var(--navy);
    text-transform: uppercase;
    line-height: 1.1;
  }
  .project-summary {
    margin: 0;
    font-family: "Lora", serif;
    font-size: 20.5px;
    line-height: 36px;
    color: var(--body-grey);
  }
  .next-button {
    position: absolute;
    left: 1055px;
    top: 398px;
    width: 100px;
    height: 100px;
  }
</style>
</head>
<body>
  <main class="slide">
    <div class="brand">
      <span class="brand-mark"></span>
      <h1 class="brand-name">Harbourline<span class="line-small">Approval Group</span></h1>
    </div>

    <section class="project">
      <h2 class="project-title">Project Title Here</h2>
      <p class="project-summary">Lorem ipsum dolor sit ispum Lorem ipsum dolor sit ispum Lorem ipsum dolor sit ispum Lorem ipsum dolor sit ispum</p>
    </section>

    <svg class="next-button" viewBox="0 0 100 100" aria-label="Next slide">
      <circle cx="50" cy="50" r="46" fill="none" stroke="var(--accent-soft)" stroke-width="4"/>
      <path d="M34 28 L76 50 L34 72 L44 50 Z" fill="var(--accent-soft)"/>
    </svg>
  </main>
</body>
</html>
```